Taking action and overcoming fear with changes in your life. Encouraging people to make a change ...

I need a logo and basic website done in wordpress for my website boldstepnow.example. I would like an image or images showing action and overcoming fear. This is an encouragement site to motivate and inspire. Images showing challenges and overcoming challenges. Bright and exciting. Please use your own creativity.

Font styles to use
Sans Serif

Colors

Designer to choose colors to be used in the design.

```html
<!DOCTYPE html>
<html lang="en">
<head>
<meta charset="utf-8">
<title>Bold Step Now</title>
<link rel="stylesheet" href="https://fonts.googleapis.com/css2?family=Jost:wght@400;500&family=Poppins:wght@400;500;600&display=swap">
<style>
:root{
  --teal:#1a8078;
  --teal-deep:#146b64;
  --teal-soft:#5cc3b8;
  --pink:#f8eaf6;
  --ink:#222;
  --muted:#555;
  --footer:#1c1c1e;
  --white:#fff;
  --cream:#f1efe9;
}
*{margin:0;padding:0;box-sizing:border-box}
html,body{width:1200px;height:3990px;overflow:hidden}
body{position:relative;font-family:"Poppins",sans-serif;color:var(--ink);background:var(--white)}
.abs{position:absolute}
h1,h2,h3,.brand,.nav a{font-family:"Jost",sans-serif;font-weight:400}

/* hero */
.hero{left:0;top:0;width:1200px;height:740px;background:linear-gradient(180deg,#4a4d6a 0%,#b0705a 35%,#d99552 55%,#8a4a2a 80%,#5a2f1c 100%)}
.hero-shade{left:600px;top:80px;width:600px;height:640px;background:radial-gradient(ellipse at 60% 60%,rgba(60,25,15,.85),rgba(60,25,15,0) 70%)}
.brand{left:145px;top:30px;font-size:40px;color:var(--white);letter-spacing:-.5px}
.nav{left:436px;top:52px;display:flex;gap:25px}
.nav a{color:var(--white);text-decoration:none;font-size:20px}
.quote-btn{left:905px;top:49px;width:151px;height:38px;border:2px solid var(--white);border-radius:20px;color:var(--white);font-size:13px;font-weight:500;display:flex;align-items:center;justify-content:center;gap:6px}
.hero-title{left:142px;top:230px;font-size:64px;line-height:78px;color:var(--white);font-weight:500}
.hero-btn{left:142px;top:408px;width:198px;height:48px;border-radius:24px;background:var(--teal);color:var(--white);font-family:"Jost",sans-serif;font-size:22px;display:flex;align-items:center;justify-content:center}
.arrow{stroke:var(--white);stroke-width:2.5;fill:none}

/* welcome */
.welcome-band{left:0;top:720px;width:1200px;height:530px;background:var(--pink)}
.welcome-photo{left:0;top:720px;width:600px;height:530px;background:linear-gradient(120deg,#5a5760,#a9a7ad 45%,#d7a57a 70%,#8b7a82)}
.welcome-title{left:611px;top:718px;font-size:35px;line-height:46px;color:var(--ink)}
.welcome-title span{font-size:40px}
.rule{height:3px;width:64px;background:var(--teal)}
.welcome-text{left:611px;top:858px;width:475px;font-size:14px;line-height:34px;color:var(--muted)}
.outline-btn{left:611px;top:1084px;width:149px;height:43px;border:2px solid var(--ink);border-radius:22px;font-size:17px;font-weight:500;display:flex;align-items:center;justify-content:center}

/* services */
.services{left:0;top:1175px;width:1200px;height:800px;background:linear-gradient(180deg,var(--teal) 0%,var(--teal-deep) 100%)}
.section-title{left:0;width:1200px;text-align:center;font-size:40px}
.svc{width:288px;background:var(--white);padding:6px 6px 20px;text-align:center}
.svc .ph{height:206px}
.svc h3{font-size:19px;margin:20px 0 10px;color:var(--ink)}
.svc p{font-size:13px;line-height:26px;color:#444;padding:0 10px}

/* help */
.help-item{width:460px;display:flex;gap:22px}
.icon{flex:none;width:102px;height:102px;border-radius:50%;border:4px solid var(--teal-soft);display:flex;align-items:center;justify-content:center}
.icon span{width:80px;height:80px;border-radius:50%;background:var(--teal-soft);display:flex;align-items:center;justify-content:center}
.help-item h3{font-size:23px;margin-bottom:6px;color:var(--ink)}
.help-item p{font-size:13.5px;line-height:26px;color:var(--muted)}
.freedom-photo{left:0;top:2540px;width:1200px;height:290px;background:linear-gradient(180deg,rgba(255,255,255,0) 0%,#8a9a8e 20%,#6f7f6a 45%,#4a5845 75%,#7b6a55 100%)}

/* news */
.news-bg{left:0;top:2800px;width:1200px;height:710px;background:var(--cream)}
.card{width:280px;background:var(--white);box-shadow:0 2px 6px rgba(0,0,0,.08)}
.card .ph{height:182px}
.card-body{display:flex;gap:12px;padding:18px 10px 22px}
.date{flex:none;width:48px;height:48px;border-radius:50%;background:var(--teal);color:var(--white);font-size:9px;line-height:13px;text-align:center;display:flex;flex-direction:column;justify-content:center}
.card h3{font-family:"Poppins",sans-serif;font-size:14px;font-weight:500;margin-bottom:4px}
.card p{font-size:10px;line-height:16px;color:var(--muted)}

/* footer */
.footer{left:0;top:3505px;width:1200px;height:485px;background:var(--footer)}
.foot-title{top:3560px;font-family:"Poppins",sans-serif;font-weight:500;font-size:19px;color:var(--white)}
.contact{left:143px;top:3617px;color:var(--white)}
.contact-row{display:flex;gap:14px;font-size:14px;line-height:24px;margin-bottom:10px}
.links a{display:block;color:var(--white);text-decoration:none;font-size:13px;line-height:30px}
.field{left:692px;width:275px;height:34px;border-radius:17px;background:var(--white);color:#555;font-size:10px;padding-left:16px;display:flex;align-items:center}
.sub-btn{left:694px;top:3772px;width:114px;height:34px;border-radius:17px;background:var(--teal);color:var(--white);font-size:12px;font-weight:600;display:flex;align-items:center;justify-content:center}
.social{left:1022px;width:33px;height:33px;border:2px solid var(--white);border-radius:50%}
.divider{left:0;top:3890px;width:1200px;height:1px;background:#333}
.copyright{left:0;top:3938px;width:1200px;text-align:center;font-size:14px;color:var(--white)}
</style>
</head>
<body>

<!-- Hero -->
<section class="abs hero" role="img" aria-label="Climbers helping each other up a cliff at sunset"></section>
<div class="abs hero-shade"></div>
<div class="abs brand">Bold Step Now</div>
<nav class="abs nav"><a>Home</a><a>About Us</a><a>Our Services</a><a>Blog</a><a>Contact</a></nav>
<div class="abs quote-btn">
  <svg width="14" height="14" viewBox="0 0 14 14"><rect x="1" y="3" width="10" height="10" fill="none" stroke="#fff" stroke-width="1.4"/><path d="M5 9 L12 2" stroke="#fff" stroke-width="1.6"/></svg>GET A QUOTE
</div>
<h1 class="abs hero-title">Encouraging People<br>To Make A Change</h1>
<div class="abs hero-btn">Get More Info</div>
<svg class="abs" style="left:68px;top:325px" width="24" height="46"><path class="arrow" d="M22 2 L2 23 L22 44"/></svg>
<svg class="abs" style="left:1105px;top:325px" width="24" height="46"><path class="arrow" d="M2 2 L22 23 L2 44"/></svg>

<!-- Welcome -->
<section class="abs welcome-band"></section>
<div class="abs welcome-photo" role="img" aria-label="Dart hitting the bullseye of a dartboard"></div>
<svg class="abs" style="left:0;top:660px" width="1200" height="80"><path d="M0 45 C250 30 500 50 800 35 C1000 25 1120 18 1200 15 L1200 80 L0 80Z" fill="var(--pink)"/><path d="M0 45 C250 30 500 50 600 45 L600 80 L0 80Z" fill="#6a6770"/></svg>
<h2 class="abs welcome-title">Welcome to<br><span>Bold Step Now</span></h2>
<div class="abs rule" style="left:611px;top:830px"></div>
<p class="abs welcome-text">Sed ut perspiciatis unde omnis iste natus error sit voluptatem accusantium doloremque laudantium, totam rem aperiam, eaque ipsa quae ab illo inventore veritatis et quasi architecto beatae vitae dicta sunt explicabo. Nemo enim ipsam voluptatem quia voluptas sit aspernatur aut odit aut fugit, sed quia consequuntur magni dolores eos qui ratione voluptatem sequi nesciunt.</p>
<div class="abs outline-btn">Read More</div>

<!-- Services -->
<section class="abs services"></section>
<svg class="abs" style="left:0;top:1170px" width="1200" height="80"><path d="M0 0 L1200 0 L1200 5 C1000 0 900 60 500 66 C250 70 100 30 0 20Z" fill="var(--pink)"/><path d="M0 0 L600 0 L600 68 C400 70 200 40 0 20Z" fill="#8b7a82"/></svg>
<h2 class="abs section-title" style="top:1295px;color:var(--white)">Our Services</h2>
<div class="abs svc" style="left:144px;top:1400px"><div class="ph" role="img" aria-label="Person standing before a giant clock" style="background:linear-gradient(160deg,#2f8aa0,#9a7a3a 55%,#4a4036)"></div><h3>Neque porro quisquam</h3><p>Sed ut perspiciatis unde omnis iste natus error sit voluptatem accusantium dolmque laudantium, totam rem aperiam, eaque ipsa quae ab illo inventore</p></div>
<div class="abs svc" style="left:457px;top:1424px"><div class="ph" role="img" aria-label="Hand holding a glowing light bulb" style="background:radial-gradient(circle at 55% 45%,#f5d7a0,#b0603a 40%,#3a2a2a 80%)"></div><h3>Neque porro quisquam</h3><p>Sed ut perspiciatis unde omnis iste natus error sit voluptatem accusantium dolmque laudantium, totam rem aperiam, eaque ipsa quae ab illo inventore</p></div>
<div class="abs svc" style="left:770px;top:1400px"><div class="ph" role="img" aria-label="Audience raising arms in celebration" style="background:linear-gradient(180deg,#d8d6d2,#7a6e68 50%,#3a3438)"></div><h3>Neque porro quisquam</h3><p>Sed ut perspiciatis unde omnis iste natus error sit voluptatem accusantium dolmque laudantium, totam rem aperiam, eaque ipsa quae ab illo inventore</p></div>
<svg class="abs" style="left:72px;top:1577px" width="24" height="46"><path class="arrow" d="M22 2 L2 23 L22 44"/></svg>
<svg class="abs" style="left:1110px;top:1577px" width="24" height="46"><path class="arrow" d="M2 2 L22 23 L2 44"/></svg>
<svg class="abs" style="left:0;top:1860px" width="1200" height="120"><path d="M0 120 L0 110 C300 110 700 120 1000 70 C1100 55 1160 20 1200 0 L1200 120Z" fill="#fff"/></svg>

<!-- Help -->
<div class="abs freedom-photo" role="img" aria-label="Woman with outstretched arms overlooking a mountain valley"></div>
<h2 class="abs section-title" style="top:2005px;font-size:42px">How We Can Help You</h2>
<div class="abs rule" style="left:562px;top:2086px;width:76px"></div>
<div class="abs help-item" style="left:144px;top:2160px"><div class="icon"><span><svg width="40" height="40" viewBox="0 0 40 40" fill="none" stroke="#fff" stroke-width="2"><circle cx="14" cy="16" r="5"/><path d="M5 34 C5 26 23 26 23 34"/><rect x="22" y="6" width="14" height="10" rx="2"/></svg></span></div><div><h3>Personal Development</h3><p>Sed ut perspiciatis unde omnis iste natus error sit voluptatem accusantium doloremque laudantium, totam rem aperiam, eaque ipsa quae ab illo inventore veritatis et quasi architecto</p></div></div>
<div class="abs help-item" style="left:640px;top:2160px"><div class="icon"><span><svg width="40" height="40" viewBox="0 0 40 40" fill="none" stroke="#fff" stroke-width="2"><path d="M10 36 L10 28 C4 24 4 10 16 6 C28 4 34 12 32 20 L34 26 L30 27 L30 33 L22 33 L22 36"/><rect x="16" y="13" width="8" height="8"/></svg></span></div><div><h3>Religion and Philosophy</h3><p>Sed ut perspiciatis unde omnis iste natus error sit voluptatem accusantium doloremque laudantium, totam rem aperiam, eaque ipsa quae ab illo inventore veritatis</p></div></div>
<div class="abs help-item" style="left:144px;top:2345px"><div class="icon"><span><svg width="40" height="40" viewBox="0 0 40 40" fill="none" stroke="#fff" stroke-width="2"><circle cx="26" cy="8" r="4"/><path d="M6 34 L6 24 L14 24 L14 18 L22 18 L22 12 L34 12 L34 34Z"/></svg></span></div><div><h3>Self Help</h3><p>Sed ut perspiciatis unde omnis iste natus error sit voluptatem accusantium doloremque laudantium, totam rem aperiam, eaque ipsa quae ab illo inventore veritatis</p></div></div>
<div class="abs help-item" style="left:640px;top:2345px"><div class="icon"><span><svg width="40" height="40" viewBox="0 0 40 40" fill="none" stroke="#fff" stroke-width="2"><rect x="12" y="6" width="16" height="12" rx="2"/><path d="M8 36 L8 22 L32 22 L32 36 M14 22 L14 32 M26 22 L26 32"/></svg></span></div><div><h3>Inspirational</h3><p>Sed ut perspiciatis unde omnis iste natus error sit voluptatem accusantium doloremque laudantium, totam rem aperiam, eaque ipsa quae ab illo inventore veritati</p></div></div>

<!-- News -->
<section class="abs news-bg"></section>
<svg class="abs" style="left:0;top:2740px" width="1200" height="100"><path d="M0 100 L0 40 C200 70 400 40 600 40 C850 40 1050 60 1200 20 L1200 100Z" fill="var(--cream)"/></svg>
<h2 class="abs section-title" style="top:2925px">Latest News</h2>
<div class="abs rule" style="left:558px;top:2987px;width:84px"></div>
<div class="abs card" style="left:142px;top:3050px"><div class="ph" role="img" aria-label="Hands assembling puzzle pieces" style="background:linear-gradient(135deg,#c69a84,#e8e0da 50%,#b88a78)"></div><div class="card-body"><div class="date">APRI 05<br>2019</div><div><h3>Nemo enim ipsam volupta</h3><p>Sed ut perspiciatis unde omnis iste natus error sit voluptatem accusantium</p></div></div></div>
<div class="abs card" style="left:458px;top:3050px"><div class="ph" role="img" aria-label="Businessman on stairs above a city skyline" style="background:linear-gradient(180deg,#f2c29a,#c98a78 50%,#5a6a7a)"></div><div class="card-body"><div class="date">APRI 05<br>2019</div><div><h3>Nemo enim ipsam volupta</h3><p>Sed ut perspiciatis unde omnis iste natus error sit voluptatem accusantium</p></div></div></div>
<div class="abs card" style="left:774px;top:3050px"><div class="ph" role="img" aria-label="Person carrying a heavy load across a tightrope" style="background:linear-gradient(180deg,#b8d0e6,#e6eef4 60%,#7a6048)"></div><div class="card-body"><div class="date">APRI 05<br>2019</div><div><h3>Nemo enim ipsam volupta</h3><p>Sed ut perspiciatis unde omnis iste natus error sit voluptatem accusantium</p></div></div></div>

<!-- Footer -->
<footer class="abs footer"></footer>
<h4 class="abs foot-title" style="left:143px">CONTACT US</h4>
<div class="abs contact">
  <div class="contact-row"><svg width="18" height="20" viewBox="0 0 18 20"><path d="M9 19 C3 12 3 9 3 8 A6 6 0 0 1 15 8 C15 9 15 12 9 19Z" fill="none" stroke="#fff" stroke-width="1.5"/><circle cx="9" cy="8" r="2" fill="#fff"/></svg><span>48 Harbor Lane<br>Westbrook, CT 06000</span></div>
  <div class="contact-row"><svg width="18" height="20" viewBox="0 0 18 20"><path d="M3 4 L6 3 L8 7 L6 9 C7 11 9 13 11 14 L13 12 L17 14 L16 17 C9 17 3 11 3 4Z" fill="none" stroke="#fff" stroke-width="1.4"/></svg><span>Phone :<br>1-(555) 014-2290</span></div>
  <div class="contact-row"><svg width="18" height="20" viewBox="0 0 18 20"><rect x="1" y="4" width="16" height="11" fill="none" stroke="#fff" stroke-width="1.4"/><path d="M1 4 L9 11 L17 4" fill="none" stroke="#fff" stroke-width="1.4"/></svg><span>Email :<br>info@boldstepnow.example</span></div>
  <div class="contact-row"><svg width="18" height="20" viewBox="0 0 18 20"><circle cx="9" cy="10" r="8" fill="#fff"/><path d="M9 5 L9 10 L12 12" stroke="#1c1c1e" stroke-width="1.6" fill="none"/></svg><span>Monday - Friday 9am - 5pm EST</span></div>
</div>
<h4 class="abs foot-title" style="left:484px">QUICK LINKS</h4>
<div class="abs links" style="left:484px;top:3610px"><a>Home</a><a>About Us</a><a>Our Services</a><a>Blog</a><a>Contact</a></div>
<h4 class="abs foot-title" style="left:692px">SIGN UP TO RECEIVE EMAIL</h4>
<p class="abs" style="left:692px;top:3605px;width:280px;font-size:10.5px;line-height:19px;color:#fff">Excepteur sint occaecat cupidatat non proident, sunt in culpa qui Nemo enim ipsam voluptatem</p>
<div class="abs field" style="top:3672px">Enter Name</div>
<div class="abs field" style="top:3720px">Enter Email</div>
<div class="abs sub-btn">SUBSCRIBE</div>
<div class="abs social" style="top:3568px"></div>
<div class="abs social" style="top:3608px"></div>
<div class="abs social" style="top:3648px"></div>
<div class="abs divider"></div>
<div class="abs copyright">Copyright © Bold Step Now 2019. All rights reserved.</div>

</body>
</html>
```